Website design for Nutraceutical Contract Manufacturer in NJ

Develop website for a contract manufacturer, specializing in nutraceutical products. Our color theme is based on the colors of the American flag (Pantone blue no. 282 & red no. 193, white), representing a US presence of a company based in Italy. Our website will include a general e-mail box link for additional info. requests, color photos of our operation, a link to our parent company's website, a video, a mission statement, a description of our capabilities.Our internet presence will be on a B2B basis, to include a map of our location and contact information.

Target Market(s)

Businesses seeking contract manufacturer in the US nutraceutical industry.

Industry/Entity Type

Manufacturer

Number of Pages Required

3 page

Font styles to use
Sans Serif

Colors
3176b5
f04a50

Requirements
Must have
• Colors, as described in project description section. Three pages minimum - one to define what we do/location/contact info,/links to affiliated companies, one to showcase certifications, one to provide photos. We are open to having additional pages as suggested, if necessary. Our website for contacts info: www.veltracore-us.com .
• Link to our general email box: info@veltracore-us.com
• Pantone colors detailed in project description.
• HTTPS secure presence
Nice to have
• TBD
Should not have
• PROFANITY

```html
<!DOCTYPE html>
<html lang="en">
<head>
<meta charset="utf-8">
<title>Veltracore US — Nutraceutical Contract Manufacturing</title>
<link rel="stylesheet" href="https://fonts.googleapis.com/css2?family=Roboto:wght@400;500;700&family=Open+Sans:wght@400;600&display=swap">
<style>
  :root {
    --blue: #3176b5;
    --blue-deep: #2a66a8;
    --red: #c0174a;
    --white: #ffffff;
    --ink: #2b2b2b;
    --ink-soft: #444b52;
    --mist: #e9eef3;
    --dark-photo: #3a3f44;
  }
  * { margin: 0; padding: 0; box-sizing: border-box; }
  html, body { width: 1200px; height: 2632px; overflow: hidden; }
  body { position: relative; font-family: "Open Sans", sans-serif; color: var(--ink); background: var(--white); }
  .section { position: absolute; left: 0; width: 1200px; overflow: hidden; }
  .heading { font-family: "Roboto", sans-serif; font-weight: 400; }
  .btn {
    position: absolute; display: flex; align-items: center; justify-content: center;
    font-family: "Roboto", sans-serif; font-weight: 500; font-size: 18px; letter-spacing: .5px;
    text-decoration: none; border: 3px solid var(--white); color: var(--white);
  }
  .btn-blue { border-color: var(--blue); color: var(--blue); }

  /* Hero */
  .hero { top: 0; height: 688px; }
  .hero-photo { position: absolute; inset: 0; background: linear-gradient(100deg, #4a5056 0%, #33383d 40%, #4f555b 65%, #d9dde0 82%, #8c9298 100%); }
  .hero-shade { position: absolute; inset: 0; background: rgba(20,24,28,.35); }
  .brand { position: absolute; left: 123px; top: 44px; display: flex; align-items: center; gap: 10px;
    font-family: "Roboto", sans-serif; font-size: 36px; font-weight: 500; color: var(--white); }
  .brand-dot { width: 14px; height: 14px; border-radius: 50%; background: var(--white); }
  .main-nav { position: absolute; top: 50px; left: 0; }
  .main-nav a, .footer-nav a { position: absolute; white-space: nowrap; font-family: "Roboto", sans-serif; text-decoration: none; }
  .main-nav a { color: var(--white); font-size: 16px; top: 0; }
  .hero-copy { position: absolute; left: 0; width: 1200px; top: 232px; text-align: center; color: var(--white); }
  .hero-kicker { font-size: 40px; line-height: 1; }
  .hero-title { font-size: 78px; line-height: 1; margin-top: 6px; letter-spacing: 1px; }
  .hero-sub { font-family: "Roboto", sans-serif; font-size: 20px; line-height: 26px; margin-top: 20px; }
  .hero .btn { left: 509px; top: 424px; width: 184px; height: 51px; font-size: 19px; }
  .slider-dots { position: absolute; top: 644px; left: 556px; display: flex; gap: 8px; }
  .slider-dots span { width: 15px; height: 15px; border-radius: 50%; background: var(--white); }
  .slider-dots span.active { background: transparent; border: 2px solid var(--white); }

  /* Mission */
  .mission { top: 688px; height: 456px; background: var(--blue); color: var(--white); }
  .video-frame { position: absolute; left: 125px; top: 70px; width: 492px; height: 291px;
    background: linear-gradient(135deg, #5d6a78 0%, #9aa6b2 45%, #c9b98a 75%, #7e8790 100%); border: 2px solid #1f4f80; }
  .play-icon { position: absolute; left: 206px; top: 105px; }
  .mission-copy { position: absolute; left: 654px; top: 72px; width: 440px; }
  .mission-copy h2 { font-size: 32px; line-height: 1; margin-bottom: 20px; }
  .mission-copy p { font-size: 14.5px; line-height: 23px; margin-bottom: 16px; }
  .mission .btn { left: 658px; top: 314px; width: 163px; height: 42px; }

  /* About */
  .about { top: 1144px; height: 477px; background: var(--mist); }
  .about-photo { position: absolute; left: 420px; top: 0; width: 780px; height: 477px;
    background: linear-gradient(90deg, var(--mist) 0%, rgba(120,128,136,.9) 22%, #4c5359 55%, #6b7278 100%); }
  .about-copy { position: absolute; left: 119px; top: 84px; width: 480px; }
  .about-copy h2 { font-size: 36px; color: #111; line-height: 1; margin-bottom: 22px; }
  .about-copy p { font-size: 14.5px; line-height: 23px; color: var(--ink-soft); margin-bottom: 14px; }
  .about .btn { left: 121px; top: 329px; width: 163px; height: 44px; }

  /* Capabilities */
  .capabilities { top: 1621px; height: 438px; }
  .capabilities-photo { position: absolute; inset: 0; background: linear-gradient(180deg, #5b8fc6 0%, #3b78b8 55%, #3070b0 100%); }
  .capabilities-tint { position: absolute; inset: 0; background: rgba(49,118,181,.55); }
  .capabilities-copy { position: absolute; left: 170px; width: 860px; top: 70px; text-align: center; color: var(--white); }
  .capabilities-copy h2 { font-size: 30px; line-height: 1; margin-bottom: 24px; }
  .capabilities-copy p { font-size: 16px; line-height: 23px; margin-bottom: 20px; }
  .capabilities .btn { left: 519px; top: 317px; width: 163px; height: 46px; }

  /* Contact */
  .contact { top: 2059px; height: 428px; }
  .contact-photo { position: absolute; inset: 0; background: linear-gradient(180deg, #c9d8e4 0%, #b7c7a8 55%, #8ea27a 100%); }
  .contact-veil { position: absolute; inset: 0; background: rgba(255,255,255,.78); }
  .contact h2 { position: absolute; top: 68px; width: 1200px; text-align: center; font-size: 30px; color: var(--red); }
  .contact-item { position: absolute; top: 153px; width: 260px; text-align: center; }
  .contact-icon { width: 88px; height: 88px; border-radius: 50%; background: var(--blue); border: 3px solid var(--white);
    box-shadow: 0 0 0 3px var(--blue); margin: 0 auto 20px; display: flex; align-items: center; justify-content: center; }
  .contact-item h3 { font-family: "Roboto", sans-serif; font-weight: 500; font-size: 18px; color: var(--blue); margin-bottom: 6px; }
  .contact-item p { font-family: "Roboto", sans-serif; font-size: 17px; line-height: 29px; color: var(--ink); }
  .contact-item a { color: var(--ink); text-decoration: none; }

  /* Footer */
  .site-footer { top: 2487px; height: 145px; background: var(--white); border-top: 1px solid #e2e2e2; }
  .footer-nav a { top: 46px; font-size: 15px; font-weight: 500; color: #111; }
  .copyright { position: absolute; left: 125px; top: 85px; font-family: "Roboto", sans-serif; font-size: 13px; color: #555; }
  .social { position: absolute; top: 47px; left: 953px; display: flex; gap: 8px; }
  .social a { width: 34px; height: 34px; border-radius: 50%; display: block; }
  .social .s1 { background: #3b5a98; }
  .social .s2 { background: #4aa3e2; }
  .social .s3 { background: var(--blue-deep); }
</style>
</head>
<body>

<header class="section hero">
  <div class="hero-photo" role="img" aria-label="Technician in hair net and blue gloves operating a production machine control panel"></div>
  <div class="hero-shade"></div>
  <div class="brand"><span class="brand-dot"></span>Veltracore US</div>
  <nav class="main-nav">
    <a href="#" style="left:491px">HOME</a>
    <a href="#" style="left:577px">ABOUT US</a>
    <a href="#" style="left:693px">AFFILIATES</a>
    <a href="#" style="left:817px">CERTIFICATIONS</a>
    <a href="#" style="left:980px">CONTACT US</a>
  </nav>
  <div class="hero-copy">
    <div class="heading hero-kicker">WELCOME TO</div>
    <h1 class="heading hero-title">VELTRACORE US</h1>
    <p class="hero-sub">Praesent elementum elit at tellus nec ultricies sit amet porttitor mattis enim<br>In massa libero interdum nec interdum vel blandit</p>
  </div>
  <a class="btn" href="#">READ MORE&nbsp;<svg width="10" height="14" viewBox="0 0 10 14"><path d="M2 2l5 5-5 5" stroke="#fff" stroke-width="2" fill="none"/></svg></a>
  <div class="slider-dots"><span class="active"></span><span></span><span></span><span></span></div>
</header>

<section class="section mission">
  <div class="video-frame" role="img" aria-label="Video still of a blister packaging line filled with softgel capsules">
    <svg class="play-icon" width="76" height="76" viewBox="0 0 76 76">
      <circle cx="38" cy="38" r="34" fill="rgba(0,0,0,.25)" stroke="#fff" stroke-width="4"/>
      <path d="M30 24l22 14-22 14z" fill="#fff"/>
    </svg>
  </div>
  <div class="mission-copy">
    <h2 class="heading">OUR MISSION</h2>
    <p>The Mission of Veltracore US is to be the premier contract manufacturer of dietary supplements in the united state, offering quality and excellence to our customers.</p>
    <p>Being a premier company does not mean being the biggest, but it does mean being the best in terms of customer service, employee talent and consistent growth</p>
  </div>
  <a class="btn" href="#">READ MORE</a>
</section>

<section class="section about">
  <div class="about-photo" role="img" aria-label="Technician in protective clothing touching a machine control screen"></div>
  <div class="about-copy">
    <h2 class="heading">ABOUT US</h2>
    <p>Fusce ultricies orci ac feugiat suscipit leo massa sodales velit et scelerisque mi tortor at ipsum cligula augue bibendum</p>
    <p>Integer congue augue et malesuada iaculis ipsum dui aliquet felis at cursus magna nisl nec elit Praesent elementum elit at tellus nec ultricies sit amet porttitor mattis enim In massa libero interdum nec interdum vel blandit sed nulla In ullamcorper est eget tempor cursus</p>
  </div>
  <a class="btn btn-blue" href="#">READ MORE</a>
</section>

<section class="section capabilities">
  <div class="capabilities-photo" role="img" aria-label="Clean production room with steel tables and stacked boxes"></div>
  <div class="capabilities-tint"></div>
  <div class="capabilities-copy">
    <h2 class="heading">OUR CAPABILITIES</h2>
    <p>Fusce ultricies orci ac feugiat suscipit leo massa sodales velit et scelerisque mi tortor at ipsum cligula augue bibendum accumsan vestibulum ut commodo a mi Morbi ornare gravida elit Integer</p>
    <p>congue augue et malesuada iaculis ipsum dui aliquet felis at cursus magna nisl nec elit Praesent elementum elit at tellus nec ultricies sit amet porttitor mattis enim In massa libero interdum nec inter</p>
    <p>Aum vel blandit sed nulla In ullamcorper est eget tempor cursus neque mi consectetuer mi</p>
  </div>
  <a class="btn" href="#">READ MORE</a>
</section>

<section class="section contact">
  <div class="contact-photo" role="img" aria-label="Company building exterior with lawn and trees"></div>
  <div class="contact-veil"></div>
  <h2 class="heading">CONTACT US</h2>
  <div class="contact-item" style="left:163px">
    <div class="contact-icon"><svg width="30" height="40" viewBox="0 0 30 40"><path d="M15 1C7 1 1 7 1 15c0 10 14 24 14 24s14-14 14-24C29 7 23 1 15 1z" fill="#fff"/><circle cx="15" cy="15" r="5" fill="#3176b5"/></svg></div>
    <h3>Our Address</h3>
    <p>72 Meridian Way Millbrook,<br>NJ 08611 USA</p>
  </div>
  <div class="contact-item" style="left:472px">
    <div class="contact-icon"><svg width="38" height="38" viewBox="0 0 24 24"><path d="M6.6 10.8a15.1 15.1 0 0 0 6.6 6.6l2.2-2.2a1 1 0 0 1 1-.25 11.4 11.4 0 0 0 3.6.57 1 1 0 0 1 1 1V20a1 1 0 0 1-1 1A17 17 0 0 1 3 4a1 1 0 0 1 1-1h3.5a1 1 0 0 1 1 1c0 1.25.2 2.45.57 3.57a1 1 0 0 1-.25 1z" fill="#fff"/></svg></div>
    <h3>Phone</h3>
    <p>+1 (609) 555-0146<br>+1 (609) 555-0182</p>
  </div>
  <div class="contact-item" style="left:779px">
    <div class="contact-icon"><svg width="38" height="30" viewBox="0 0 38 30"><rect x="1" y="1" width="36" height="28" rx="3" fill="#fff"/><path d="M2 3l17 13L36 3" stroke="#3176b5" stroke-width="3" fill="none"/></svg></div>
    <h3>Email Us</h3>
    <p><a href="mailto:info@veltracore-us.com">info@veltracore-us.com</a></p>
  </div>
</section>

<footer class="section site-footer">
  <nav class="footer-nav">
    <a href="#" style="left:125px">HOME</a>
    <a href="#" style="left:205px">ABOUT US</a>
    <a href="#" style="left:314px">AFFILIATES</a>
    <a href="#" style="left:431px">CERTIFICATIONS</a>
    <a href="#" style="left:588px">CONTACT US</a>
  </nav>
  <p class="copyright">© 2018 Company Name &nbsp;All right reserved</p>
  <div class="social">
    <a class="s1" href="#" aria-label="Social profile one"></a>
    <a class="s2" href="#" aria-label="Social profile two"></a>
    <a class="s3" href="#" aria-label="Social profile three"></a>
  </div>
</footer>

</body>
</html>
```